Business Card Design

We just need these details on one side of card and logo on the other.

Industry/Entity Type

Business

Contact Information for Business Card

Colette Marsh | Artist
87 Tillbrook Lane
Dunmore Heights Vic 3172
# 0418 207 913 | 03 9386 2417
colette@colettemarsh-example.com
colettesstudio-example.com.au

```html
<!DOCTYPE html>
<html lang="en">
<head>
<meta charset="utf-8">
<title>Colette Marsh | Artist — Business Card</title>
<link rel="stylesheet" href="https://fonts.googleapis.com/css2?family=Pathway+Gothic+One&display=swap">
<style>
  :root {
    --card-bg: #ffffff;
    --ink: #111111;
  }
  html, body {
    margin: 0;
    padding: 0;
    width: 1200px;
    height: 741px;
    overflow: hidden;
    background: var(--card-bg);
  }
  .card {
    position: relative;
    width: 1200px;
    height: 741px;
    background: var(--card-bg);
    color: var(--ink);
    font-family: "Pathway Gothic One", "Arial Narrow", sans-serif;
  }
  .card__line {
    position: absolute;
    left: 0;
    width: 1200px;
    margin: 0;
    text-align: center;
    white-space: nowrap;
    line-height: 1;
    font-weight: 400;
  }
  .card__title {
    top: 188px;
    font-size: 122px;
    letter-spacing: 0.005em;
  }
  .card__address {
    top: 354px;
    font-size: 52px;
  }
  .card__phones {
    top: 425px;
    font-size: 41px;
    letter-spacing: 0.3em;
  }
  .card__email {
    top: 476px;
    font-size: 40px;
    letter-spacing: 0.14em;
  }
  .card__web {
    top: 520px;
    font-size: 38px;
    display: flex;
    justify-content: center;
    align-items: center;
    gap: 10px;
  }
  .card__ornament {
    display: inline-block;
    width: 20px;
    height: 14px;
    border-radius: 3px;
    background: var(--ink);
  }
</style>
</head>
<body>
  <main class="card">
    <h1 class="card__line card__title">Colette Marsh | Artist</h1>
    <p class="card__line card__address">87 Tillbrook Lane Dunmore Heights Vic 3172</p>
    <p class="card__line card__phones"># 0418 207 913 | 03 9386 2417</p>
    <p class="card__line card__email">colette@colettemarsh-example.com</p>
    <p class="card__line card__web">
      <span class="card__ornament" role="img" aria-label="Small bird silhouette ornament"></span>
      <span>colettesstudio-example.com.au</span>
      <span class="card__ornament" role="img" aria-label="Small bird silhouette ornament"></span>
    </p>
  </main>
</body>
</html>
```